50th Anniversary Gala Save the date Postcard 8.5x5.5 inches

Looking for a 5.5x8.5 in one-sided postcard design for our annual gala. Design needs to include "Save the date" prominently with all the event information included below. Design should be light, include the colors of our logo and elegant. (almost like a wedding save the date). "Bridges of Grace" should look like its own logo.

50th Anniversary Gala at The Lodge at Birchmere Glen – “Bridges of Grace – Celebrating 50 Years of Building Community”
Thursday, October 24
6-11p
The Lodge at Birchmere Glen
Calloway Parkway, Maple Hollow, NY
Honoring – TRB Previous Presidents

Target Market(s)

Exisiting donors

Industry/Entity Type

nonprofit

Font styles to use
Serif
Script

Requirements
Must have
• Save the date prominent
Should not have
• should not have a dark background

```html
<!DOCTYPE html>
<html lang="en">
<head>
<meta charset="utf-8">
<title>50th Anniversary Gala – Save the Date</title>
<link rel="stylesheet" href="https://fonts.googleapis.com/css2?family=Josefin+Sans:wght@300;400&family=Montserrat:wght@500;600;700;800&family=Permanent+Marker&family=Poppins:wght@400;500;700&display=swap">
<style>
  :root{
    --stage:#ececec;
    --paper:#ffffff;
    --navy:#0d2a55;
    --blue:#1e8fd5;
    --green:#6aae3e;
    --gold:#c9a23c;
    --gold-light:#e8cf7a;
    --ink:#333a44;
    --peach:#f4a48e;
    --wash-blue:#cfe6ef;
  }
  *{margin:0;padding:0;box-sizing:border-box}
  html,body{width:902px;height:1200px;overflow:hidden;background:var(--stage)}
  .postcard{
    position:absolute;left:21px;top:322px;width:860px;height:556px;
    background:var(--paper);box-shadow:0 4px 14px rgba(0,0,0,.18);overflow:hidden;
  }
  .postcard svg{display:block;width:860px;height:556px}
  .label-sans{font-family:"Montserrat",sans-serif}
  .label-geo{font-family:"Josefin Sans",sans-serif}
  .label-brush{font-family:"Permanent Marker",cursive}
  .label-body{font-family:"Poppins",sans-serif}
</style>
</head>
<body>
<main class="postcard">
<svg viewBox="0 0 860 556" xmlns="http://www.w3.org/2000/svg">
  <defs>
    <linearGradient id="goldFoil" x1="0" y1="0" x2="1" y2="1">
      <stop offset="0" stop-color="#e6c86a"/>
      <stop offset=".5" stop-color="#c99b2e"/>
      <stop offset="1" stop-color="#e8d38a"/>
    </linearGradient>
    <radialGradient id="peachWash" cx=".5" cy=".5" r=".5">
      <stop offset="0" stop-color="var(--peach)" stop-opacity=".85"/>
      <stop offset="1" stop-color="var(--peach)" stop-opacity="0"/>
    </radialGradient>
    <radialGradient id="blueWash" cx=".5" cy=".5" r=".5">
      <stop offset="0" stop-color="var(--wash-blue)" stop-opacity=".8"/>
      <stop offset="1" stop-color="var(--wash-blue)" stop-opacity="0"/>
    </radialGradient>
  </defs>

  <!-- watercolour floral decoration -->
  <g class="floral-wash" role="img" aria-label="Soft watercolour wash in peach and pale blue tones">
    <ellipse cx="120" cy="40" rx="170" ry="90" fill="url(#blueWash)"/>
    <ellipse cx="760" cy="110" rx="160" ry="130" fill="url(#blueWash)"/>
    <ellipse cx="430" cy="330" rx="220" ry="120" fill="url(#peachWash)" opacity=".25"/>
  </g>
  <g class="floral-corner" role="img" aria-label="Watercolour coral flower at top right corner">
    <ellipse cx="840" cy="80" rx="55" ry="75" fill="url(#peachWash)"/>
  </g>
  <g class="floral-corner" role="img" aria-label="Watercolour coral flowers and grey leaves at bottom left corner">
    <ellipse cx="50" cy="490" rx="100" ry="95" fill="url(#peachWash)"/>
    <ellipse cx="18" cy="398" rx="30" ry="18" fill="#9fb3c0" opacity=".6"/>
    <ellipse cx="10" cy="344" rx="14" ry="16" fill="#f2c36a" opacity=".6"/>
  </g>
  <g class="floral-corner" role="img" aria-label="Watercolour peach flower at bottom right corner">
    <ellipse cx="820" cy="520" rx="95" ry="70" fill="url(#peachWash)" opacity=".6"/>
  </g>

  <!-- headline -->
  <text class="label-sans" x="430" y="60" text-anchor="middle" font-size="21" font-weight="700" fill="var(--navy)" letter-spacing="8">SAVE THE DATE</text>
  <text class="label-geo" x="74" y="236" font-size="228" font-weight="300" fill="url(#goldFoil)" textLength="228" lengthAdjust="spacingAndGlyphs">50</text>
  <text class="label-sans" x="306" y="108" font-size="44" font-weight="600" fill="url(#goldFoil)" textLength="50" lengthAdjust="spacingAndGlyphs">TH</text>
  <text class="label-sans" x="352" y="231" font-size="128" font-weight="700" fill="var(--blue)" textLength="333" lengthAdjust="spacingAndGlyphs">GALA</text>
  <text class="label-brush" font-family="'Permanent Marker', cursive" x="358" y="146" font-size="72" fill="var(--green)" textLength="424" lengthAdjust="spacingAndGlyphs" transform="rotate(-3 570 120)">Anniversary</text>

  <!-- venue band -->
  <rect x="76" y="248" width="705" height="39" fill="var(--navy)"/>
  <path d="M116 257a7 7 0 0 1 7 7c0 5-7 12-7 12s-7-7-7-12a7 7 0 0 1 7-7z" fill="var(--gold)"/>
  <circle cx="116" cy="264" r="2.6" fill="var(--navy)"/>
  <text class="label-sans" x="136" y="277" font-size="24" font-weight="600" fill="#fff" textLength="628" lengthAdjust="spacing">AT THE LODGE AT BIRCHMERE GLEN</text>

  <!-- theme lockup -->
  <text class="label-sans" x="75" y="353" font-size="36" font-weight="800" fill="var(--blue)" textLength="347" lengthAdjust="spacingAndGlyphs">BRIDGES OF GRACE</text>
  <text class="label-brush" font-family="'Permanent Marker', cursive" x="74" y="406" font-size="42" fill="var(--green)" textLength="200" lengthAdjust="spacingAndGlyphs">Celebrating</text>
  <text class="label-geo" x="290" y="443" font-size="112" font-weight="300" fill="url(#goldFoil)" textLength="112" lengthAdjust="spacingAndGlyphs">50</text>
  <text class="label-sans" x="357" y="410" font-size="21" font-weight="600" fill="var(--gold)" textLength="70" lengthAdjust="spacingAndGlyphs">YEARS</text>
  <text class="label-body" x="74" y="439" font-size="15" font-weight="500" fill="var(--ink)" textLength="204" lengthAdjust="spacingAndGlyphs">OF BUILDING COMMUNITY</text>

  <line x1="455" y1="322" x2="455" y2="442" stroke="#dddddd" stroke-width="1.5"/>

  <!-- date block -->
  <rect x="492" y="321" width="92" height="90" fill="var(--navy)"/>
  <text class="label-body" x="538" y="383" text-anchor="middle" font-size="58" font-weight="700" fill="#fff">24</text>
  <text class="label-body" x="538" y="403" text-anchor="middle" font-size="14" font-weight="500" fill="var(--gold-light)">OCTOBER</text>
  <rect x="595" y="321" width="186" height="41" fill="url(#goldFoil)"/>
  <text class="label-sans" x="688" y="350" text-anchor="middle" font-size="23" font-weight="600" fill="#fff" letter-spacing="3">THURSDAY</text>
  <text class="label-geo" x="595" y="412" font-size="56" font-weight="400" fill="var(--navy)" textLength="186" lengthAdjust="spacingAndGlyphs">6-11PM</text>
  <path d="M499 421a5.5 5.5 0 0 1 5.5 5.5c0 4-5.5 9.5-5.5 9.5s-5.5-5.5-5.5-9.5a5.5 5.5 0 0 1 5.5-5.5z" fill="var(--gold)"/>
  <circle cx="499" cy="426.5" r="2" fill="#fff"/>
  <text class="label-body" x="510" y="435" font-size="19" font-weight="400" fill="var(--navy)" textLength="271" lengthAdjust="spacingAndGlyphs">The Lodge at Birchmere Glen</text>

  <!-- address and honourees -->
  <path d="M181 473a5 5 0 0 1 5 5c0 3.5-5 8.5-5 8.5s-5-5-5-8.5a5 5 0 0 1 5-5z" fill="var(--gold)"/>
  <circle cx="181" cy="478" r="1.8" fill="#fff"/>
  <text class="label-body" x="190" y="488" font-size="16" font-weight="700" fill="var(--navy)" textLength="307" lengthAdjust="spacingAndGlyphs">Calloway Parkway, Maple Hollow, NY</text>
  <rect x="176" y="496" width="79" height="17" fill="url(#goldFoil)"/>
  <text class="label-sans" x="215.5" y="509" text-anchor="middle" font-size="11" font-weight="700" fill="var(--navy)">HONORING</text>
  <text class="label-body" x="265" y="509" font-size="11" font-weight="400" fill="var(--ink)" textLength="226" lengthAdjust="spacingAndGlyphs">CALLOWAY PARKWAY, MAPLE HOLLOW, NY</text>

  <line x1="510" y1="473" x2="510" y2="519" stroke="#dddddd" stroke-width="1.5"/>

  <!-- host organisation -->
  <circle cx="541" cy="490" r="9" fill="var(--gold)"/>
  <text class="label-body" x="555" y="487" font-size="12" font-weight="700" fill="var(--navy)">Harborlight</text>
  <text class="label-body" x="555" y="502" font-size="12" font-weight="700" fill="var(--navy)">Alliance</text>
</svg>
</main>
</body>
</html>
```